Stone Over Tide - Stationery Design Project

Hi everyone,

We need a business card and a stationary set designed for a new corporate video production company based in Sydney, 'Stone Over Tide'.

The name refers to the mythological 'phoenix' so we would like to see designs that are appropriate to both the name and to a creative film company. The key thing is, we need to appear fresh and creative while maintaining professionalism.

We would like to stick with dark colors for the basis of the card. One idea that came up was obsidian/volcanic rock with the logo cracking through to reveal lava or something fire like. This is just one idea that has come up, but we are of course open to others and would love to see what people can come up with. Extensive use of flames/fire imagery is not really what we are after.

Also, cinematic as opposed to corporate is preferable.

**** UPDATE ****
When I hand over the card to a prospective client, I want them to feel like they are receiving an obsidian plate with inscriptions in it (ie the phoenix). Looking for something elemental and rigid to contrast and complement the graceful lines of the logo.

Designs we require:
- Business card
(We would like a business card that makes use of some of the more premium business card printing options, such as foil stamping, embossing/debossing, painted edges, spot UV etc. Doesnt have to use all these things, only what you feel works, but we are looking for a business card that stands out and is memorable and these nice touches have that effect. For an example of what is possible, check out "http://www.velvetprintery.net/base/category/business-card-gallery/".)

- Letter head
- With compliments slip
- Display folder

COPMPANY DETAILS:
ABN: 62 738 294 019
Company Address: 7/18-20 Kell St, Marbury NSW 2058
Name: Rex M. Dunleavy
Title: Producer
Contact Number: 0412 539 204
email: rex@stoneovertide.com
website: www.stoneovertide.com

ABOUT THE PHOENIX:
The phoenix is a musical bird from mythology, known for its long fancy tail and small plume on the top of its head. They are elegant and graceful and symbolize immortality, endurance and strength, believed to live for 5 centuries before they were reborn from their ashes.
Updates

Hi everyone,

We have just updated the design brief to include business contact information, website etc. should anyone require it for their designs.

Thanks

Rex

Target Market(s)

Other creative businesses and marketing firms.

Industry/Entity Type

Printing

Requirements
Must have
• Basic printing requirements:
- CMYK colour space
- 300dpi resolution
- Color bleed/crop marks etc to allow for trimming where necessary
- Source files upon handover
Should not have
• Overuse of fire/flame imagery

```html
<!DOCTYPE html>
<html lang="en">
<head>
<meta charset="utf-8">
<title>Stone Over Tide – Business Card</title>
<link rel="stylesheet" href="https://fonts.googleapis.com/css2?family=Marcellus&display=swap">
<style>
  :root {
    --backdrop: #c9c9c9;
    --card-light: #2a2e3a;
    --card-dark: #0b0d16;
    --sheen: rgba(255,255,255,0.07);
    --ink-white: #f2f2f2;
    --ink-grey: #9a9ea6;
    --ink-name: #8d9397;
    --ink-soft: #b9bdc1;
    --accent-red: #e0202a;
  }
  * { margin: 0; padding: 0; box-sizing: border-box; }
  html, body {
    width: 1200px; height: 1000px; overflow: hidden;
    background: var(--backdrop);
    font-family: "Marcellus", serif;
  }
  .canvas { position: relative; width: 1200px; height: 1000px; }

  .card {
    position: absolute;
    border-radius: 40px;
    overflow: hidden;
    background: linear-gradient(125deg, var(--card-light) 0%, #151824 45%, var(--card-dark) 100%);
  }
  .card-front { left: 282px; top: 77px; width: 611px; height: 393px; }
  .card-back  { left: 275px; top: 521px; width: 613px; height: 399px; }

  .card-art { position: absolute; inset: 0; width: 100%; height: 100%; }

  .wordmark {
    position: absolute;
    color: var(--ink-white);
    white-space: nowrap;
    text-transform: uppercase;
  }
  .card-front .wordmark {
    left: 0; right: 0; top: 295px;
    text-align: center;
    font-size: 26px; letter-spacing: 9px;
  }
  .card-back .wordmark {
    left: 0; width: 360px; top: 194px;
    text-align: center;
    font-size: 17px; letter-spacing: 6px;
  }

  .address {
    position: absolute; left: 0; width: 340px; top: 242px;
    text-align: center; color: var(--ink-grey);
    font-size: 19px; line-height: 21px; text-transform: uppercase;
  }
  .abn {
    position: absolute; left: 0; width: 340px; top: 292px;
    text-align: center; color: var(--ink-soft);
    font-size: 16px; letter-spacing: 0.5px;
  }
  .website {
    position: absolute; left: 58px; top: 338px;
    color: var(--accent-red); font-size: 17px; letter-spacing: 0.5px;
    text-transform: uppercase;
  }

  .person {
    position: absolute; right: 47px; top: 70px; text-align: right;
  }
  .person-name {
    color: var(--ink-name); font-size: 22px; letter-spacing: 0.5px;
    text-transform: uppercase;
  }
  .person-title {
    color: #6f7478; font-size: 13px; letter-spacing: 1px;
    text-transform: uppercase; margin-top: 2px;
  }

  .contact {
    position: absolute; right: 47px; top: 311px; text-align: right;
    color: var(--ink-soft); font-size: 17px; line-height: 22px; letter-spacing: 0.5px;
  }
  .contact-label { color: #7d8287; }
</style>
</head>
<body>
<main class="canvas">

  <section class="card card-front" aria-label="Business card front">
    <svg class="card-art" viewBox="0 0 611 393" aria-hidden="true">
      <path d="M0 0 H90 C150 40 170 150 230 250 C280 330 360 380 470 393 H0 Z" fill="var(--sheen)"/>
      <circle cx="305" cy="205" r="7" fill="var(--accent-red)"/>
      <ellipse cx="305" cy="266" rx="45" ry="2.5" fill="#000" opacity="0.55"/>
    </svg>
    <div class="wordmark">Stone Over Tide</div>
  </section>

  <section class="card card-back" aria-label="Business card back">
    <svg class="card-art" viewBox="0 0 613 399" aria-hidden="true">
      <circle cx="250" cy="230" r="240" fill="none" stroke="#2b2f3a" stroke-width="6"/>
      <circle cx="255" cy="235" r="225" fill="none" stroke="#22252f" stroke-width="3"/>
      <circle cx="180" cy="120" r="6" fill="var(--accent-red)"/>
      <ellipse cx="166" cy="175" rx="34" ry="2" fill="#000" opacity="0.55"/>
    </svg>
    <div class="wordmark">Stone Over Tide</div>
    <div class="address">7/18-20 Kell St<br>Marbury NSW 2058</div>
    <div class="abn">ABN 62 738 294 019</div>
    <div class="website">www.stoneovertide.com</div>

    <div class="person">
      <div class="person-name">Rex M. Dunleavy</div>
      <div class="person-title">Producer</div>
    </div>
    <div class="contact">
      <div><span class="contact-label">T</span> 0412 539 204</div>
      <div><span class="contact-label">E</span> rex@stoneovertide.com</div>
    </div>
  </section>

</main>
</body>
</html>
```